Business Card design for an International Import Export House

We need a Business Card design for our import export business. We trade in Minerals, Metals, Rice, Sugar, Steel etc.. The design should be minimalistic. It may or may not contain the physical address. In case you want to include the physical address - 418 Verandah Heights, Marlow Sector 9, Kestrelton, Westmark, Avalis, 480215.

Target Market(s)

Steel Mills or Steel Plants, Factories, Mining businesses, Industrial houses, Government Agencies

Industry/Entity Type

Importer

Contact Information for Business Card

Business Name - Tessan Overseas

Font styles to use
Other font styles liked:
• montserrat

Requirements
Must have
• Ravi Kandola - President
• www.tessanoverseas.com
• ravi@tessanoverseas.com
• +91-987-654-3217
Nice to have
• global traders of raw minerals

```html
<!DOCTYPE html>
<html lang="en">
<head>
<meta charset="utf-8">
<title>Tessan Overseas – Business Card</title>
<link rel="stylesheet" href="https://fonts.googleapis.com/css2?family=Montserrat:wght@500;700&family=Open+Sans:wght@400;600&display=swap">
<style>
  :root {
    --page-bg: #2b2b2d;
    --teal: #3b97ad;
    --teal-dark: #2f7f94;
    --teal-light: #4aa8bb;
    --teal-pale: #a9d9e3;
    --card-white: #f3f6fa;
    --ink: #44505a;
    --ink-soft: #5e6a73;
  }
  * { box-sizing: border-box; margin: 0; padding: 0; }
  html, body { width: 1200px; height: 879px; overflow: hidden; }
  body {
    background: var(--page-bg);
    display: flex;
    flex-direction: column;
    align-items: center;
    justify-content: center;
    gap: 56px;
    font-family: "Open Sans", Arial, sans-serif;
  }
  .card {
    position: relative;
    width: 630px;
    height: 360px;
    border-radius: 3px;
    overflow: hidden;
    box-shadow: 0 14px 30px rgba(0,0,0,.45);
  }

  /* Back side */
  .card-back {
    background: linear-gradient(135deg, var(--teal-dark) 0%, var(--teal) 55%, var(--teal-light) 100%);
    display: flex;
    flex-direction: column;
    align-items: center;
    justify-content: center;
    gap: 14px;
  }
  .card-back .brand-mark { border-color: var(--teal-pale); }
  .card-back .brand-name { color: var(--teal-pale); font-size: 22px; }
  .tagline {
    color: var(--teal-pale);
    font-family: "Open Sans", Arial, sans-serif;
    font-size: 19px;
    letter-spacing: 1.5px;
    margin-top: 6px;
  }

  /* Brand block (shared) */
  .brand {
    display: flex;
    flex-direction: column;
    align-items: center;
    gap: 12px;
  }
  .brand-mark {
    width: 78px;
    height: 78px;
    border: 4px solid var(--teal);
    border-radius: 50%;
  }
  .brand-name {
    font-family: "Montserrat", Arial, sans-serif;
    font-weight: 700;
    font-size: 19px;
    letter-spacing: -0.3px;
    color: var(--teal);
    white-space: nowrap;
  }

  /* Front side */
  .card-front { background: var(--card-white); }
  .card-front .brand {
    position: absolute;
    left: 36px;
    top: 92px;
  }
  .person {
    position: absolute;
    right: 40px;
    top: 38px;
    text-align: right;
  }
  .person-name {
    font-family: "Montserrat", Arial, sans-serif;
    font-weight: 700;
    font-size: 25px;
    color: var(--teal);
    letter-spacing: .3px;
  }
  .person-title {
    font-family: "Open Sans", Arial, sans-serif;
    font-size: 17px;
    color: var(--ink-soft);
    letter-spacing: 1.5px;
    margin-top: 2px;
  }
  .contacts {
    position: absolute;
    right: 30px;
    top: 146px;
    list-style: none;
  }
  .contacts li {
    display: flex;
    align-items: center;
    justify-content: flex-end;
    gap: 14px;
    font-size: 14.5px;
    color: var(--ink);
    line-height: 21px;
  }
  .icon { width: 14px; height: 14px; fill: var(--teal); flex: none; }
  .pin {
    position: absolute;
    right: 30px;
    top: 222px;
    width: 16px;
    height: 20px;
    fill: var(--teal);
  }
  .rule {
    position: absolute;
    left: 0;
    right: 0;
    top: 250px;
    height: 4px;
    background: var(--teal);
  }
  .address {
    position: absolute;
    left: 36px;
    bottom: 36px;
    font-size: 14.5px;
    color: var(--ink);
    letter-spacing: .3px;
    white-space: nowrap;
  }
  .base-rule {
    position: absolute;
    left: 0;
    right: 0;
    bottom: 18px;
    height: 3px;
    background: var(--teal);
  }
</style>
</head>
<body>

  <section class="card card-back" aria-label="Card back">
    <div class="brand">
      <span class="brand-mark"></span>
      <span class="brand-name">TESSAN OVERSEAS</span>
    </div>
    <p class="tagline">global traders of raw minerals</p>
  </section>

  <section class="card card-front" aria-label="Card front">
    <div class="brand">
      <span class="brand-mark"></span>
      <span class="brand-name">TESSAN OVERSEAS</span>
    </div>

    <div class="person">
      <h1 class="person-name">RAVI KANDOLA</h1>
      <p class="person-title">PRESIDENT</p>
    </div>

    <ul class="contacts">
      <li>+91-987-654-3217
        <svg class="icon" viewBox="0 0 24 24" aria-hidden="true"><path d="M6.6 10.8a15.1 15.1 0 0 0 6.6 6.6l2.2-2.2a1 1 0 0 1 1-.25 11.4 11.4 0 0 0 3.6.57 1 1 0 0 1 1 1V20a1 1 0 0 1-1 1A17 17 0 0 1 3 4a1 1 0 0 1 1-1h3.5a1 1 0 0 1 1 1c0 1.25.2 2.45.57 3.57a1 1 0 0 1-.25 1z"/></svg>
      </li>
      <li>tessanoverseas.com
        <svg class="icon" viewBox="0 0 24 24" aria-hidden="true"><path d="M12 2a10 10 0 1 0 0 20 10 10 0 0 0 0-20zm6.9 6h-3a15.6 15.6 0 0 0-1.4-3.6A8 8 0 0 1 18.9 8zM12 4c.8 1.2 1.5 2.5 1.9 4h-3.8c.4-1.5 1.100-2.8 1.9-4zM4.3 14a8 8 0 0 1 0-4h3.4a16 16 0 0 0 0 4zm.8 2h3a15.6 15.6 0 0 0 1.4 3.6A8 8 0 0 1 5.1 16zm3-8h-3a8 8 0 0 1 4.4-3.6C8.9 5.5 8.4 6.7 8.1 8zM12 20c-.8-1.2-1.5-2.5-1.9-4h3.8c-.4 1.5-1.1 2.8-1.9 4zm2.3-6H9.7a14.5 14.5 0 0 1 0-4h4.6a14.5 14.5 0 0 1 0 4zm.2 5.6c.6-1.1 1.1-2.3 1.4-3.6h3a8 8 0 0 1-4.4 3.6zm1.8-5.6a16 16 0 0 0 0-4h3.4a8 8 0 0 1 0 4z"/></svg>
      </li>
      <li>ravi@tessanoverseas.com
        <svg class="icon" viewBox="0 0 24 24" aria-hidden="true"><path d="M2 5h20v14H2zm2 2v.4l8 5 8-5V7zm0 2.8V17h16V9.8l-8 5z"/></svg>
      </li>
    </ul>

    <svg class="pin" viewBox="0 0 16 20" aria-hidden="true"><path d="M8 0a7 7 0 0 0-7 7c0 5 7 13 7 13s7-8 7-13a7 7 0 0 0-7-7zm0 10a3 3 0 1 1 0-6 3 3 0 0 1 0 6z"/></svg>
    <div class="rule"></div>

    <p class="address">418 Verandah Heights, Marlow Sector 9, Kestrelton, Westmark, Avalis, 480215</p>
    <div class="base-rule"></div>
  </section>

</body>
</html>
```